Flyer-Design für Arztpraxis
Zielgruppe
Es handelt sich um eine Arztpraxis für innere Medizin und hausärztlicher Versorgung. Der Schwerpunkt ist jedoch die Diagnostik und Vorsorge von Herz und Gefäßerkrankungen.
Der Flyer soll als Information über die Leistungen und Angebote dienen.
Aufgabenstellung
Das Design sollte schlicht und modern sein. Ein Logo ist bereits vorhanden (siehe Dateiupload). Diese Farben sollten sich auch im kompletten Flyer-Design wiederfinden.
Die Fotos dienen nur zur Orientierung. Es besteht hier noch nicht die endgültige Einrichtung, da die Praxis noch im Umbau ist.

```html
<!DOCTYPE html>
<html lang="de">
<head>
<meta charset="utf-8">
<title>Praxis Lukas Hendriks – Flyer</title>
<link href="https://fonts.googleapis.com/css2?family=Roboto+Slab:wght@400;500;700&family=Roboto:wght@300;400;500&family=Open+Sans:wght@400&display=swap" rel="stylesheet">
<style>
  :root {
    --panel: #d2e6f8;
    --panel-circle: #c0dbf2;
    --blue: #3d87c0;
    --orange: #f0a020;
    --text: #222;
    --muted: #555;
    --rule: #a9c4da;
    --white: #fff;
  }
  * { margin: 0; padding: 0; box-sizing: border-box; }
  html, body { width: 1200px; height: 932px; overflow: hidden; background: var(--white); }
  .flyer { position: relative; width: 1200px; height: 932px; overflow: hidden; font-family: "Roboto", sans-serif; }

  .services { position: absolute; left: 0; top: 0; width: 400px; height: 932px; background: var(--panel); overflow: hidden; }
  .circle { position: absolute; border-radius: 50%; background: var(--panel-circle); }
  .circle.top { left: 306px; top: -55px; width: 190px; height: 190px; }
  .circle.bottom { left: -115px; top: 670px; width: 320px; height: 225px; border-radius: 50%; width: 225px; left: -20px; }
  .circle.small { left: 110px; top: 900px; width: 66px; height: 66px; }

  .services h1 { position: absolute; left: 50px; top: 108px; font-family: "Roboto Slab", serif; font-weight: 400; font-size: 24px; color: var(--blue); letter-spacing: 0.3px; }
  .service-list { position: absolute; left: 50px; top: 210px; width: 300px; list-style: none; font-family: "Open Sans", sans-serif; font-size: 12px; color: var(--text); }
  .service-list li { height: 30px; line-height: 30px; border-bottom: 1px solid var(--rule); }
  .service-list li:last-child { border-bottom: none; }

  .extras { position: absolute; left: 50px; top: 431px; width: 300px; height: 346px; background: var(--white); padding: 46px 32px 0; }
  .extras h2 { font-family: "Roboto Slab", serif; font-weight: 400; font-size: 15px; line-height: 23px; color: var(--orange); margin-bottom: 20px; }
  .extras ul { list-style: none; font-family: "Open Sans", sans-serif; font-size: 12px; color: var(--text); width: 234px; }
  .extras li { border-bottom: 1px solid #ddd; padding: 6px 0; line-height: 18px; }
  .extras li.group { line-height: 30px; padding: 0 0 2px; }
  .extras li:last-child { border-bottom: none; }

  .map { position: absolute; left: 436px; top: 14px; width: 316px; height: 320px; background: linear-gradient(135deg, #eef5fb, #dcebf7); }

  .directions { position: absolute; left: 450px; top: 380px; width: 320px; }
  .directions h2 { font-family: "Roboto Slab", serif; font-weight: 500; font-size: 18px; color: var(--orange); margin-bottom: 26px; }
  .directions p { font-weight: 300; font-size: 13px; line-height: 24px; color: var(--muted); }

  .contact { position: absolute; left: 449px; top: 598px; font-size: 13px; line-height: 24px; color: var(--muted); font-weight: 300; }
  .contact h3 { font-family: "Roboto Slab", serif; font-weight: 500; font-size: 13.5px; color: var(--blue); }
  .contact dl { display: grid; grid-template-columns: 63px auto; }
  .contact dt { font-family: "Roboto Slab", serif; font-weight: 500; font-size: 12px; color: var(--blue); }

  .brand { position: absolute; left: 815px; top: 88px; display: flex; align-items: center; gap: 22px; }
  .brand-dot { width: 76px; height: 76px; border-radius: 50%; background: var(--blue); }
  .brand-name { font-family: "Roboto Slab", serif; font-weight: 500; font-size: 19px; color: var(--blue); line-height: 22px; }
  .brand-sub { font-size: 12px; letter-spacing: 1.6px; color: var(--muted); margin-top: 2px; }

  .photo { position: absolute; left: 796px; top: 214px; width: 404px; height: 613px; background: linear-gradient(120deg, #c99a6e 0%, #e7dfd6 28%, #f4f6f8 45%, #8cc6ee 62%, #5aa8de 100%); }

  .footer { position: absolute; left: 400px; top: 827px; width: 800px; height: 105px; background: var(--blue); }
  .footer dl { position: absolute; left: 445px; top: 27px; display: grid; grid-template-columns: 54px auto; font-size: 13.5px; line-height: 22px; color: var(--white); letter-spacing: 0.4px; }
</style>
</head>
<body>
<div class="flyer">
  <section class="services">
    <div class="circle top"></div>
    <div class="circle bottom"></div>
    <div class="circle small"></div>
    <h1>LEISTUNGSSPEKTRUM</h1>
    <ul class="service-list">
      <li>Herz-Kreislauf-Untersuchungen</li>
      <li>EKG, Belastungs-EKG, Langzeit-EKG und Langzeit-RR</li>
      <li>Ultraschalluntersuchungen</li>
      <li>Bauch, Schilddrüse, Lunge</li>
      <li>Gesundheitsvorsorge ab 35 Jahren</li>
    </ul>
    <div class="extras">
      <h2>INDIVIDUELLE<br>GESUNDHEITSLEISTUNGEN</h2>
      <ul>
        <li class="group">Duplexsonographie<br>(periphere Arterien und Venene/<br>hirnversorgende Gefäße)</li>
        <li>Echokardiographie</li>
        <li>Neuraltherapie</li>
        <li>Gesundheitsuntersuchungen und Labor</li>
      </ul>
    </div>
  </section>

  <div class="map" role="img" aria-label="Lageplan der Praxis mit umliegenden Straßen und Standortmarkierung"></div>

  <section class="directions">
    <h2>ANFAHRT</h2>
    <p>Halltestelle Lindenhof, Bus 550 und 551<br>halten direkt vor unserem Haus.<br>Parkplätze sind liegen hinter dem Haus und<br>sind über den Birkenweg zu erreichen.</p>
  </section>

  <section class="contact">
    <h3>PRAXIS LUKAS HENDRIKS</h3>
    <p>Facharzt für Innere Medizin<br>Lindenallee 12<br>58999 Talbrück</p>
    <dl>
      <dt>TEL.</dt><dd>01234 56 78 900</dd>
      <dt>FAX</dt><dd>01234 56 78 910</dd>
      <dt>E-MAIL</dt><dd>info@praxis-hendriks.de</dd>
    </dl>
  </section>

  <header class="brand">
    <div class="brand-dot"></div>
    <div>
      <div class="brand-name">PRAXIS LUKAS HENDRIKS</div>
      <div class="brand-sub">FACHARZT FÜR INNERE MEDIZIN</div>
    </div>
  </header>

  <div class="photo" role="img" aria-label="Foto: Stethoskop auf blauem Arztkittel und Rezeptblock auf Holztisch"></div>

  <footer class="footer">
    <dl>
      <dt>TEL.</dt><dd>01234 56 78 900</dd>
      <dt>E-MAIL</dt><dd>INFO@PRAXIS-HENDRIKS.DE</dd>
    </dl>
  </footer>
</div>
</body>
</html>
```